3 Page Design for Northbrook Capital

We want a Home Page, About Page, and Products & Services Page for Northbrook Capital. Please refer to the attached docs for more info.
If done in Figma, would like Figma files that can easily be ported to Wordpress.

```html
<!DOCTYPE html>
<html lang="en">
<head>
<meta charset="utf-8">
<title>Northbrook Capital — Home</title>
<link href="https://fonts.googleapis.com/css2?family=Inter+Tight:wght@300;400;500;600;700;800&display=swap" rel="stylesheet">
<style>
:root{
  --purple:#5e4f8d;
  --red:#9a1b34;
  --dark:#2c2c2c;
  --ink:#1e1e1e;
  --muted:#444;
  --beige:#ede2cf;
  --ring:#e5d8c2;
  --white:#fff;
}
*{box-sizing:border-box;margin:0;padding:0}
html,body{width:1200px;height:3108px;overflow:hidden}
body{font-family:"Inter Tight",Arial,sans-serif;color:var(--ink);background:var(--white);position:relative}
a{color:inherit;text-decoration:none}

/* header */
.topbar{position:absolute;left:0;top:0;width:1200px;height:6px;background:var(--dark)}
.contact-strip{position:absolute;top:0;left:540px;width:660px;height:56px;background:var(--dark);
  clip-path:polygon(0 0,100% 0,100% 100%,40px 100%);display:flex;align-items:center;justify-content:flex-end;padding-right:128px;gap:34px;color:#fff;font-size:18px}
.contact-strip span{display:flex;align-items:center;gap:10px}
.contact-strip .sep{opacity:.8}
.brand{position:absolute;left:110px;top:82px;display:flex;align-items:center;gap:10px;font-weight:700;font-size:22px;color:var(--dark)}
.brand-dot{width:18px;height:18px;border-radius:50%;background:var(--red)}
.nav{position:absolute;top:96px;left:403px;display:flex;gap:44px;font-size:15px;font-weight:500}
.nav .active{color:var(--purple)}
.btn{display:inline-block;background:var(--red);color:#fff;font-weight:600;border-radius:3px;letter-spacing:-.2px}
.nav-cta{position:absolute;left:875px;top:87px;width:214px;height:41px;line-height:41px;text-align:center;font-size:17px}

/* hero */
.hero{position:absolute;top:151px;left:0;width:1200px;height:557px;
  background:linear-gradient(100deg,#7c7a3e 0%,#8a8549 20%,#3e4a3a 40%,#6f7771 60%,#c8ccd0 80%,#eef0f2 100%)}
.hero-box{position:absolute;left:567px;top:116px;width:544px;height:311px;background:rgba(100,100,100,.92);color:#fff;padding:22px 18px}
.hero-box h1{font-size:42px;line-height:54px;font-weight:700;letter-spacing:-1.2px}
.hero-box p{font-size:16.5px;line-height:26px;font-weight:300;margin-top:14px;letter-spacing:-.4px}
.hero-btn{display:inline-block;margin-top:20px;margin-left:3px;background:var(--purple);color:#fff;font-weight:600;font-size:17px;width:134px;height:42px;line-height:42px;text-align:center;border-radius:3px}

/* story */
.eyebrow{font-size:17px;font-weight:400;color:var(--ink);letter-spacing:-.2px}
.h2{font-size:35px;font-weight:700;color:var(--purple);letter-spacing:-1px}
.rule{width:56px;height:4px;background:var(--red)}
.story{position:absolute;top:831px;left:110px;width:450px}
.story .h2{margin-top:12px}
.story .rule{margin:12px 0 0 8px}
.story .copy{margin:34px 0 0 8px;width:430px;font-size:14.5px;line-height:27.5px;font-weight:300;color:var(--muted);letter-spacing:-.4px}
.story .copy p+p{margin-top:27px}
.story .btn{margin:38px 0 0 7px;width:133px;height:42px;line-height:42px;text-align:center;font-size:17px}
.story-visual{position:absolute;left:580px;top:760px;width:420px;height:500px;border-radius:50% 50% 50% 50%/40% 40% 60% 60%;
  background:radial-gradient(circle at 50% 40%,#6f7f98 0%,#2e3f5c 45%,#8f8f8f 78%,#e6dac6 100%)}

/* framework */
.framework{position:absolute;top:1410px;left:0;width:1200px;text-align:center}
.framework .h2{margin-top:14px}
.framework .rule{margin:18px auto 0}
.steps{position:absolute;top:155px;left:0;width:1200px}
.step{position:absolute;width:210px;text-align:center}
.step .ring{width:145px;height:145px;border-radius:50%;border:3px solid var(--ring);margin:0 auto;display:flex;align-items:center;justify-content:center;background:#fff}
.step .ring.lift{border-color:#fff;box-shadow:0 4px 18px rgba(0,0,0,.12)}
.step h3{margin-top:22px;font-size:15.5px;font-weight:600;letter-spacing:-.3px}

/* mission */
.mission{position:absolute;top:1879px;left:0;width:1200px;height:482px;background:var(--beige)}
.mission .inner{position:absolute;left:114px;top:56px;width:560px}
.mission .h2{margin-top:14px}
.mission .rule{margin-top:16px;margin-left:1px}
.mission .copy{margin-top:37px;width:530px;font-size:17px;line-height:27.5px;letter-spacing:-.3px;color:var(--ink)}
.mission .copy strong{font-weight:700}
.mission .copy p+p{margin-top:27px}

/* cta */
.cta{position:absolute;top:2432px;left:0;width:1200px;text-align:center}
.cta .h2{font-size:34px}
.cta .rule{margin:20px auto 0}
.cta p{margin:28px auto 0;width:820px;font-size:14.5px;line-height:25.5px;font-weight:300;color:var(--muted);letter-spacing:-.4px}
.cta .btn{margin-top:29px;width:228px;height:43px;line-height:43px;font-size:17px}

/* footer */
.footer{position:absolute;top:2723px;left:0;width:1200px;height:385px;background:var(--dark);color:#fff}
.footer-brand{position:absolute;left:114px;top:100px;display:flex;align-items:center;gap:14px;font-size:30px;font-weight:700}
.footer-brand .brand-dot{width:26px;height:26px;background:#fff}
.footer h4{font-size:21px;font-weight:600;letter-spacing:-.5px}
.links{position:absolute;left:491px;top:76px}
.links ul{list-style:none;margin-top:22px}
.links li{font-size:15px;height:34px;line-height:34px}
.reach{position:absolute;left:763px;top:76px}
.reach ul{list-style:none;margin-top:20px}
.reach li{font-size:15px;height:46px;display:flex;align-items:center;gap:14px;letter-spacing:-.3px}
.reach svg{flex:none}
.footer hr{position:absolute;left:110px;top:301px;width:980px;border:0;border-top:1px solid #8a8a8a}
.copyright{position:absolute;top:339px;width:1200px;text-align:center;font-size:15px;letter-spacing:-.3px}
</style>
</head>
<body>

<header>
  <div class="topbar"></div>
  <div class="contact-strip">
    <span><svg width="18" height="14" viewBox="0 0 18 14"><rect width="18" height="14" rx="1" fill="#fff"/><path d="M1 1l8 6 8-6" stroke="#2c2c2c" stroke-width="1.6" fill="none"/></svg>info@northbrookcapital.com</span>
    <span class="sep">|</span>
    <span><svg width="16" height="16" viewBox="0 0 24 24"><path fill="#fff" d="M6.6 10.8a15 15 0 006.6 6.6l2.2-2.2a1 1 0 011-.25 11.4 11.4 0 003.6.57 1 1 0 011 1V20a1 1 0 01-1 1A17 17 0 013 4a1 1 0 011-1h3.5a1 1 0 011 1c0 1.25.2 2.45.57 3.57a1 1 0 01-.25 1z"/></svg>+1 888-888-8888</span>
  </div>
  <a class="brand" href="#"><span class="brand-dot"></span>Northbrook Capital</a>
  <nav class="nav">
    <a class="active" href="#">Home</a>
    <a href="#">About Us</a>
    <a href="#">Products &amp; Services</a>
    <a href="#">Contact Us</a>
  </nav>
  <a class="btn nav-cta" href="#">Start Your Next Chapter</a>
</header>

<section class="hero" role="img" aria-label="Photo of a smiling couple running together on a hillside road at sunset">
  <div class="hero-box">
    <h1>Built for Legacy.<br>Designed for Performance</h1>
    <p>A modern wealth advisory helping individuals, families, and business owners build, protect, and multiply their financial future — one smart decision at a time.</p>
    <a class="hero-btn" href="#">Get Started</a>
  </div>
</section>

<section class="story">
  <div class="eyebrow">VISUAL STORY</div>
  <h2 class="h2">Your Wealth Has Momentum</h2>
  <div class="rule"></div>
  <div class="copy">
    <p>Most people play the game of life only through the first four chapters — reacting to deadlines, bills, and short-term goals.<br>But real wealth is built in the next chapter — the space where strategy, discipline, and clarity come together.</p>
    <p>We guide you through a structured, repeatable process so your wealth grows consistently — regardless of your starting point.</p>
  </div>
  <a class="btn" href="#">Read More</a>
</section>
<div class="story-visual" role="img" aria-label="Photo of a bearded advisor in a navy suit holding a tablet"></div>

<section class="framework">
  <div class="eyebrow">OFFER FRAMEWORK</div>
  <h2 class="h2">Our Framework for Financial Success</h2>
  <div class="rule"></div>
  <div class="steps">
    <div class="step" style="left:81px">
      <div class="ring"><svg width="70" height="70" viewBox="0 0 70 70" fill="none" stroke="#9a1b34" stroke-width="3"><rect x="10" y="10" width="50" height="50" rx="6" transform="rotate(45 35 35)"/><circle cx="35" cy="35" r="12" fill="#9a1b34"/><path d="M29 35l4 4 8-8" stroke="#fff"/></svg></div>
      <h3>Clarify Your Position</h3>
    </div>
    <div class="step" style="left:288px">
      <div class="ring lift"><svg width="60" height="74" viewBox="0 0 60 74" fill="none" stroke="#5e4f8d" stroke-width="2.6"><circle cx="28" cy="30" r="22"/><circle cx="28" cy="30" r="14"/><circle cx="28" cy="30" r="6"/><path d="M28 30L50 8M44 8h6v6"/><path d="M20 54h16v8H20zM22 66h12"/></svg></div>
      <h3>Define the Target</h3>
    </div>
    <div class="step" style="left:494px">
      <div class="ring"><svg width="84" height="74" viewBox="0 0 84 74" fill="none" stroke="#9a1b34" stroke-width="2.6"><path d="M6 8h10v60H6zM16 14h62v54H16"/><path d="M26 32h8M26 42h14M26 52h20"/><circle cx="62" cy="48" r="8"/><path d="M52 34l18-18 6 6-18 18"/></svg></div>
      <h3>Strategic Blueprint</h3>
    </div>
    <div class="step" style="left:702px">
      <div class="ring"><svg width="76" height="76" viewBox="0 0 76 76" fill="none" stroke="#9a1b34" stroke-width="2.6"><circle cx="38" cy="38" r="24"/><circle cx="38" cy="38" r="15"/><path d="M31 38l5 5 10-10"/><path d="M38 6v8M38 62v8M6 38h8M62 38h8M15 15l6 6M55 55l6 6M61 15l-6 6M21 55l-6 6"/></svg></div>
      <h3>Execution &amp; Accountability</h3>
    </div>
    <div class="step" style="left:909px">
      <div class="ring"><svg width="76" height="72" viewBox="0 0 76 72" fill="none" stroke="#9a1b34" stroke-width="2.6"><path d="M4 68h68"/><rect x="10" y="50" width="9" height="18"/><rect x="24" y="40" width="9" height="28"/><rect x="38" y="30" width="9" height="38"/><rect x="52" y="18" width="9" height="50"/><path d="M8 40l18-14 12 6 24-22M54 10h8v8"/></svg></div>
      <h3>Growth &amp; Optimization</h3>
    </div>
  </div>
</section>

<section class="mission">
  <div class="inner">
    <div class="eyebrow">ABOUT US</div>
    <h2 class="h2">MISSION</h2>
    <div class="rule"></div>
    <div class="copy">
      <p>At Northbrook Capital, we believe every financial journey deserves a strategy built on clarity, resilience, and intentional planning.<br>Our mission is simple:<br><strong>To empower people to own their wealth story — not just react to it.</strong></p>
      <p>Through smart frameworks, disciplined guidance, and data-backed insights, we help you build wealth that lasts beyond seasons, cycles, and circumstances.</p>
    </div>
  </div>
</section>

<section class="cta">
  <h2 class="h2">Ready to build the wealth you were meant for?</h2>
  <div class="rule"></div>
  <p>Sed ut perspiciatis unde omnis iste natus error sit voluptatem accusantium doloremque laudantium, totam rem aperiam, eaque ipsa quae ab illo inventore veritatis et quasi architecto beatae vitae dicta sunt explicabo.</p>
  <a class="btn" href="#">Begin Your Next Chapter</a>
</section>

<footer class="footer">
  <div class="footer-brand"><span class="brand-dot"></span>Northbrook Capital</div>
  <div class="links">
    <h4>Quick Links</h4>
    <ul><li>Home</li><li>About</li><li>Products &amp; Services</li><li>Contact Us</li></ul>
  </div>
  <div class="reach">
    <h4>Get In Touch</h4>
    <ul>
      <li><svg width="12" height="16" viewBox="0 0 12 16"><path fill="#fff" d="M6 0a6 6 0 00-6 6c0 4.5 6 10 6 10s6-5.5 6-10a6 6 0 00-6-6zm0 8.5A2.5 2.5 0 118.5 6 2.5 2.5 0 016 8.5z"/></svg>35448 Nemo enim ipsam voluptatem quia</li>
      <li><svg width="16" height="12" viewBox="0 0 18 14"><rect width="18" height="14" rx="1" fill="#fff"/><path d="M1 1l8 6 8-6" stroke="#2c2c2c" stroke-width="1.6" fill="none"/></svg>info@northbrookcapital.com</li>
      <li><svg width="13" height="13" viewBox="0 0 24 24"><path fill="#fff" d="M6.6 10.8a15 15 0 006.6 6.6l2.2-2.2a1 1 0 011-.25 11.4 11.4 0 003.6.57 1 1 0 011 1V20a1 1 0 01-1 1A17 17 0 013 4a1 1 0 011-1h3.5a1 1 0 011 1c0 1.25.2 2.45.57 3.57a1 1 0 01-.25 1z"/></svg>+1 888-888-8888</li>
    </ul>
  </div>
  <hr>
  <div class="copyright">Copyright 2025. Company Name.All Rights Reserved</div>
</footer>

</body>
</html>
```